Local Electrical company need some kick ass business cards

In need of some in your face design business cards for a family owned electrical service company in Edmonton, Alberta Canada. We provide reliable and trustworthy electrical service for commercial and residential work in the Edmonton and area. We have been in business for 25 years.

Target Market(s)

Residential and commercial electrical

Industry/Entity Type

Business

Contact Information for Business Card

Your welcome to change and modify the Vantor Wiring logo. please include the lightbulb! Our Colours are black and green please stay with that.
Please include a name phone number and address on the card
phone number - 780-555-0138
#22, 418 Maple Ridge Rd, St.Albert, Alberta.
Two things that need to be on the card.
"your friendly neighborhood electrictrician"
Commercial & residential electrical repair and service

Colors
9bcb3c

Requirements
Must have
• Light bulb guy Attached
• "your friendly neighborhood electrictrician"
• Commercial & residential electrical repair and service
• phone number - 780-555-0138
• #22, 418 Maple Ridge Rd, St.Albert, Alberta.
• Our colours are black and green
Nice to have
• go wild i want something loud

```html
<!DOCTYPE html>
<html lang="en">
<head>
<meta charset="utf-8">
<title>Vantor Wiring – Business Card</title>
<link rel="stylesheet" href="https://fonts.googleapis.com/css2?family=Open+Sans:wght@400;600;700&display=swap">
<style>
  :root {
    --bg: #d9d9d9;
    --black: #050505;
    --strip: #161616;
    --white: #ffffff;
    --green: #9bcb3c;
    --text: #f2f2f2;
  }
  * { box-sizing: border-box; margin: 0; padding: 0; }
  html, body {
    width: 1200px; height: 900px; overflow: hidden;
    background: var(--bg);
    font-family: "Open Sans", Arial, sans-serif;
  }
  .sheet {
    width: 1200px; height: 900px;
    display: flex; flex-direction: column; align-items: center; justify-content: center;
    gap: 40px;
  }
  .card {
    position: relative;
    width: 700px; height: 400px;
    background: var(--black);
    overflow: hidden;
    box-shadow: 0 6px 18px rgba(0,0,0,0.25);
  }
  .band-white {
    position: absolute; left: 0; right: 0; top: 330px; height: 10px;
    background: var(--white);
  }
  .band-green {
    position: absolute; left: 0; right: 0; top: 340px; bottom: 0;
    background: var(--green);
  }

  /* Front */
  .mascot {
    position: absolute; left: 130px; top: 30px;
    width: 125px; height: 175px;
    border-radius: 55px 55px 28px 28px;
    background: linear-gradient(160deg, #9bcb3c 0%, #e6eef4 35%, #b9c6cf 75%, #6f7a82 100%);
  }
  .tagline {
    position: absolute; left: 285px; top: 140px;
    color: var(--text); font-weight: 600; font-size: 16px; line-height: 1.3;
  }
  .tagline span { display: block; }
  .tagline .first { padding-left: 55px; }
  .services {
    position: absolute; left: 100px; top: 288px;
    color: var(--white); font-weight: 700; font-size: 18px; white-space: nowrap;
  }

  /* Back */
  .contact-strip {
    position: absolute; left: 0; right: 0; top: 225px; height: 105px;
    background: var(--strip);
  }
  .brand {
    position: absolute; left: 60px; top: 150px;
    display: flex; align-items: center; gap: 10px;
    color: var(--green); font-weight: 700; font-size: 30px; letter-spacing: 0.5px;
  }
  .brand-dot {
    width: 16px; height: 16px; border-radius: 50%; background: var(--green);
  }
  .person {
    position: absolute; right: 58px; top: 100px; text-align: right;
  }
  .person-name { color: var(--green); font-size: 24px; font-weight: 600; letter-spacing: 0.5px; }
  .person-role { color: var(--text); font-size: 18px; }
  .contact {
    position: absolute;
    color: var(--text); font-size: 15px; line-height: 1.75;
  }
  .contact-address { left: 40px; top: 240px; }
  .contact-phones { left: 295px; top: 260px; }
  .contact-online { left: 470px; top: 275px; }
  .contact-line { display: flex; align-items: center; gap: 7px; white-space: nowrap; }
  .icon { width: 14px; height: 14px; flex: none; fill: var(--green); }
</style>
</head>
<body>
<main class="sheet">

  <section class="card card-front">
    <div class="mascot" role="img" aria-label="Cartoon light bulb mascot wearing a green cap"></div>
    <p class="tagline">
      <span class="first">your friendly</span>
      <span>neighborhood electrictrician</span>
    </p>
    <p class="services">Commercial &amp; Residential Electrical Repair and Service</p>
    <div class="band-white"></div>
    <div class="band-green"></div>
  </section>

  <section class="card card-back">
    <div class="brand"><span class="brand-dot"></span>Vantor Wiring</div>
    <div class="person">
      <p class="person-name">MARCUS HALE</p>
      <p class="person-role">Managing Director</p>
    </div>
    <div class="contact-strip"></div>

    <div class="contact contact-address">
      <p class="contact-line">
        <svg class="icon" viewBox="0 0 14 14"><path d="M7 0a5 5 0 0 0-5 5c0 3.6 5 9 5 9s5-5.4 5-9a5 5 0 0 0-5-5zm0 7a2 2 0 1 1 0-4 2 2 0 0 1 0 4z"/></svg>
        #22, 418 Maple Ridge Rd,
      </p>
      <p class="contact-line">St.Albert, Alberta.</p>
    </div>

    <div class="contact contact-phones">
      <p class="contact-line">
        <svg class="icon" viewBox="0 0 14 14"><path d="M1 4c0-1.5 2.5-3 6-3s6 1.5 6 3v1h-3V4H4v1H1zM3 6h8l1 6H2z"/></svg>
        780-555-0138
      </p>
      <p class="contact-line">
        <svg class="icon" viewBox="0 0 14 14"><path d="M4 0h6a1 1 0 0 1 1 1v12a1 1 0 0 1-1 1H4a1 1 0 0 1-1-1V1a1 1 0 0 1 1-1zm0 2v9h6V2z"/></svg>
        780-555-0138
      </p>
    </div>

    <div class="contact contact-online">
      <p class="contact-line">
        <svg class="icon" viewBox="0 0 14 14"><path d="M0 2h14v10H0zm1.5 1.5L7 8l5.5-4.5z"/></svg>
        info@vantorwiring.ca
      </p>
      <p class="contact-line">
        <svg class="icon" viewBox="0 0 14 14"><path d="M5.5 8.5l3-3M6 3.5l1.5-1.5a2.5 2.5 0 0 1 3.5 3.5L9.5 7M8 10.5L6.5 12A2.5 2.5 0 0 1 3 8.5L4.5 7" stroke="#9bcb3c" stroke-width="1.8" fill="none" stroke-linecap="round"/></svg>
        www.vantorwiring.ca
      </p>
    </div>

    <div class="band-white"></div>
    <div class="band-green"></div>
  </section>

</main>
</body>
</html>
```